Web Design for historic veg friendly, organic restaurant

We need a new web site. The Brookmere Cafe is a 40 year old restaurant in Chicago. We've been one of the premier, casual vegetarian restaurants since we opened. 5 years ago, Brookmere Cafe was purchased from the original owners by a local, certified organic farmer. We are nearly 100% from scratch kitchen, 100% certified organic produce, we are governed by a strict sustainable plan and we are very active politically. But you wouldn't know it form our website! We have a desire to build a simple website around some basic principles:
1. We need our current logo prominently displayed (logo attached)
2. We need a "click to call" easily accessible
3. We have an online order link that needs to be easily accessible
4. We need our hours, location, and directions easy to see
4. We need a separate events page (we have a live music and events venue that runs shows 5-7 nights per week.)
5. We would like to have a separate page for pictures, particularly old pictures. It would be fun to have a function for people to post their own shots, but that might make this too complicated. If it were possible, we would of course need to retain the ability to curate posted pictures.
6. This needs to be easily edited by us, so in a platform such as word press or similar
7. We will need this mobile enhanced

Target Market(s)

Neighborhood residents - zip code is 60626

Industry/Entity Type

Restaurant

Coding

Coded - Design and coding required

Number of Pages Required

4 page

Font styles to use
Sans Serif

Requirements
Must have
• Logo, click to call, events page that we can manage, contact us, about us page, menu (we have the online menu through a third party plugin), a page for our market and some nice pictures on our splash page,
• Must be mobile ready and on a platform such as Word Press or some other platform where we can edit on our own
Nice to have
• Page for past employees and historical pictures, be nice to have food pictures or something similar on a scroll, would love to have an ability for others to post pictures that we would "approve"
Should not have
• We don't need anything that spins, moves, flames or other features that detract from gathering information

```html
<!DOCTYPE html>
<html lang="en">
<head>
<meta charset="utf-8">
<title>News &amp; Events – Brookmere Cafe</title>
<link rel="stylesheet" href="https://fonts.googleapis.com/css2?family=Catamaran:wght@400;500;600&family=Crimson+Text&family=Raleway:wght@400;500&family=Roboto:wght@400;500&display=swap">
<style>
:root{
  --ink:#111;
  --text:#444;
  --muted:#666;
  --page:#f4f4f4;
  --card:#fff;
  --line:#e6e6e6;
  --yellow:#fdde1a;
  --black:#000;
  --white:#fff;
}
*{box-sizing:border-box;margin:0;padding:0}
html,body{width:814px;height:1200px;overflow:hidden}
body{position:relative;background:var(--page);font-family:'Raleway',sans-serif;color:var(--text)}
.site-header{position:absolute;top:0;left:0;width:814px;height:45px;background:var(--white)}
.brand{position:absolute;left:82px;top:0;width:96px;height:54px;background:var(--white);box-shadow:0 1px 4px rgba(0,0,0,.18);display:flex;align-items:center;justify-content:center;gap:4px;z-index:2}
.brand-mark{width:8px;height:8px;background:#c8201e}
.brand-name{font-family:'Catamaran',sans-serif;font-weight:600;font-size:12px;line-height:1;color:#c8201e;text-align:center}
.main-nav{position:absolute;right:82px;top:15px;display:flex;gap:19px;font-family:'Roboto',sans-serif;font-size:9.5px;color:#222}
.hero-band{position:absolute;top:45px;left:0;width:814px;height:35px;background:linear-gradient(90deg,#5a3b2a,#9a7c62 30%,#d8d0c4 55%,#b79a73 80%,#6d5038)}
.page-title{position:absolute;top:104px;width:814px;text-align:center;font-family:'Catamaran',sans-serif;font-weight:600;font-size:37px;line-height:1;color:var(--ink)}
.page-sub{position:absolute;top:144px;width:814px;text-align:center;font-family:'Catamaran',sans-serif;font-size:15px;color:#555}
.grid{position:absolute;top:185px;left:66px;display:flex;gap:17px}
.col{width:158px;display:flex;flex-direction:column;gap:28px}
.col.c3 .card:last-child{margin-top:-4px}
.card{background:var(--card);box-shadow:0 1px 2px rgba(0,0,0,.06)}
.photo{height:105px}
.photo.short{height:88px}
.card-body{padding:14px 14px 0}
.tags{display:flex;flex-wrap:wrap;gap:5px}
.tag{font-size:6.2px;text-transform:uppercase;border:1px solid var(--line);border-radius:10px;padding:4px 9px;color:#333}
.card h2{font-family:'Crimson Text',serif;font-weight:400;font-size:15.5px;line-height:17.5px;color:var(--ink);margin:11px 0 14px}
.excerpt{font-size:8.3px;line-height:13px;color:#444;padding:0 3px}
.keywords{font-size:5.8px;line-height:13px;text-transform:uppercase;color:#444;margin:10px 3px 8px}
.meta{border-top:1px solid var(--line);margin:0 -14px;padding:8px 17px 8px;font-size:5.8px;text-transform:uppercase;color:#444}
.load-more{position:absolute;top:907px;left:379px;width:56px;height:13px;background:var(--yellow);font-family:'Roboto',sans-serif;font-weight:500;font-size:7.5px;color:#111;text-align:center;line-height:13px;border-radius:2px}
.newsletter{position:absolute;top:988px;left:0;width:814px;height:60px;background:var(--yellow)}
.nl-title{position:absolute;left:110px;top:18px;display:flex;align-items:center;gap:5px;font-family:'Catamaran',sans-serif;font-weight:500;font-size:19px;color:#111}
.nl-field{position:absolute;left:394px;top:13px;width:211px;height:34px;background:var(--white);font-family:'Raleway',sans-serif;font-style:italic;font-size:9px;color:#999;padding:11px 8px}
.nl-btn{position:absolute;left:605px;top:13px;width:101px;height:34px;background:var(--black);color:var(--yellow);font-family:'Roboto',sans-serif;font-weight:500;font-size:11px;text-align:center;line-height:34px}
.site-footer{position:absolute;top:1048px;left:0;width:814px;height:152px;background:var(--black);color:var(--white);font-family:'Roboto',sans-serif;text-align:center}
.connect{position:absolute;top:20px;width:100%;font-size:12.5px}
.social{position:absolute;top:42px;left:0;width:100%;display:flex;justify-content:center;gap:4px}
.social span{width:15px;height:15px;border-radius:50%;background:var(--white)}
.foot-nav{position:absolute;top:69px;width:100%;font-size:8px;word-spacing:1px}
.foot-nav b{font-weight:400;margin:0 8px}
.foot-rule{position:absolute;top:86px;left:110px;width:595px;height:1px;background:#999}
.pin{position:absolute;top:93px;left:402px}
.address{position:absolute;top:110px;width:100%;font-size:7.8px;font-family:'Raleway',sans-serif}
.copyright{position:absolute;top:125px;width:100%;font-size:7.3px;font-family:'Raleway',sans-serif}
</style>
</head>
<body>
<header class="site-header">
  <div class="brand"><span class="brand-mark"></span><span class="brand-name">Brookmere<br>Cafe</span></div>
  <nav class="main-nav"><span>Homes</span><span>About</span><span>Menu</span><span>Reservation</span><span>Gallery</span><span>Contact</span></nav>
</header>
<div class="hero-band" role="img" aria-label="Table with chopsticks, rice and ginger"></div>

<h1 class="page-title">News &amp; Events</h1>
<p class="page-sub">Today Specials</p>

<main class="grid">
  <div class="col">
    <article class="card">
      <div class="photo" role="img" aria-label="Lamb chops with rosemary in a skillet" style="background:linear-gradient(135deg,#5b4536,#2a211c 55%,#7a6a5c)"></div>
      <div class="card-body">
        <div class="tags"><span class="tag">Recipes</span><span class="tag">Tips &amp; Tricks</span></div>
        <h2>Which Lamb is the Best: American, Australian or New Zealand?</h2>
        <p class="excerpt">Lamb is a very subjective item. Many people feel that New Zealand or Australian is…</p>
        <p class="keywords">Bio, Dinner, Food, Hand Made, Lamb, Recipe, Tricks</p>
        <div class="meta">Lena Harlow &nbsp;·&nbsp; 27 Sep, 2014 &nbsp;·&nbsp; ○ 1</div>
      </div>
    </article>
    <article class="card">
      <div class="photo short" role="img" aria-label="Breakfast table with pastries and juice" style="background:linear-gradient(135deg,#e9dfcf,#c9a56e 50%,#f2ece2)"></div>
      <div class="card-body">
        <div class="tags"><span class="tag">Tips &amp; Tricks</span></div>
        <h2>Breakfast Interrupted</h2>
        <p class="excerpt">One of our most recent shoots, titled Breakfast Interrupted, is now live for your viewing…</p>
        <p class="keywords">Food, Hand Made, Tips, Tricks, Video</p>
        <div class="meta">Lena Harlow &nbsp;·&nbsp; 9 Mar, 2014 &nbsp;·&nbsp; ○ 6</div>
      </div>
    </article>
  </div>

  <div class="col">
    <article class="card">
      <div class="photo" role="img" aria-label="Copper cup cocktail with fresh mint" style="background:linear-gradient(135deg,#2b2b2b,#8a5a3c 55%,#1d1d1d)"></div>
      <div class="card-body">
        <div class="tags"><span class="tag">Healthy Food</span><span class="tag">Recipes</span></div>
        <h2>The Caipirinha Is The Brazilian Cocktail You’ve Been Too Afraid To Pronounce</h2>
        <p class="excerpt">It’s time to take a break from the mojito, put down the margarita, and give…</p>
        <p class="keywords">Cocktail, Food, Healthy, Recipe</p>
        <div class="meta">Lena Harlow &nbsp;·&nbsp; 1 Sep, 2014 &nbsp;·&nbsp; ○ 0</div>
      </div>
    </article>
    <article class="card">
      <div class="photo" role="img" aria-label="Person working on a laptop in a cafe" style="background:linear-gradient(135deg,#2c2824,#6b5d50 50%,#1e1c1a)"></div>
      <div class="card-body">
        <div class="tags"><span class="tag">Tips &amp; Tricks</span></div>
        <h2>The coffice: the future of work?</h2>
        <p class="excerpt">Still toiling away in a grey office building? Boring! According to Corvo’s ‘soonologist’, you’ll get…</p>
        <p class="keywords">Coffee, Tips, Tricks</p>
        <div class="meta">Lena Harlow &nbsp;·&nbsp; 10 Mar, 2014 &nbsp;·&nbsp; ○ 3</div>
      </div>
    </article>
  </div>

  <div class="col c3">
    <article class="card">
      <div class="photo" role="img" aria-label="Toasts with plum jam on a wooden board" style="background:linear-gradient(135deg,#3a3330,#7a5a48 50%,#2c2623)"></div>
      <div class="card-body">
        <div class="tags"><span class="tag">Cooking</span><span class="tag">Healthy Food</span></div>
        <h2>The Plum Recipes That’ll Make You Fall In Love With This Stone Fruit</h2>
        <p class="excerpt">It’s easy to forget about plums. They’re not the most popular of summer fruits. Plums…</p>
        <p class="keywords">Cooking, Healthy, Plum, Recipe</p>
        <div class="meta">Lena Harlow &nbsp;·&nbsp; 23 Mar, 2014 &nbsp;·&nbsp; ○ 0</div>
      </div>
    </article>
    <article class="card">
      <div class="photo" role="img" aria-label="Lattice berry tart on a dark table" style="background:linear-gradient(135deg,#1f2420,#b99248 50%,#2a2a26)"></div>
      <div class="card-body">
        <div class="tags"><span class="tag">Cooking</span><span class="tag">Recipes</span></div>
        <h2>40 Truly Amazing Blueberry Recipes YUM!</h2>
        <p class="excerpt">We have blueberries to thank for some of our favorite foods. What would mornings be…</p>
        <p class="keywords">Blueberry, Cooking, Experiments, Healthy, Recipe</p>
        <div class="meta">Lena Harlow &nbsp;·&nbsp; 10 Mar, 2014 &nbsp;·&nbsp; ○ 0</div>
      </div>
    </article>
  </div>

  <div class="col">
    <article class="card">
      <div class="photo" role="img" aria-label="Fresh figs on a white board" style="background:linear-gradient(135deg,#f1efec,#d8c8c0 55%,#f7f6f4)"></div>
      <div class="card-body">
        <div class="tags"><span class="tag">Cooking</span><span class="tag">Healthy Food</span><span class="tag">Recipes</span></div>
        <h2>24 Reasons To Seek Out Fresh Figs</h2>
        <p class="excerpt">Dried figs are great and all, but if you’ve ever tasted a fresh fig you…</p>
        <p class="keywords">Cooking, Food, Healthy, Tips, Tricks</p>
        <div class="meta">Lena Harlow &nbsp;·&nbsp; 22 Mar, 2014 &nbsp;·&nbsp; ○ 0</div>
      </div>
    </article>
    <article class="card">
      <div class="photo short" role="img" aria-label="Video still of fresh strawberries for a granita recipe" style="background:linear-gradient(135deg,#2a3a2a,#a8262a 55%,#1e2a1e)"></div>
      <div class="card-body">
        <div class="tags"><span class="tag">Tips &amp; Tricks</span></div>
        <h2>Now You’re Cooking – Strawberry Granita</h2>
        <p class="excerpt">One out of eight films created for Kelvane’ ‘Now You’re Cooking’ campaign.</p>
        <p class="keywords">Granita, Recipe, Strawberry, Tips, Tricks</p>
        <div class="meta">Lena Harlow &nbsp;·&nbsp; 20 Mar, 2014 &nbsp;·&nbsp; ○ 0</div>
      </div>
    </article>
  </div>
</main>

<div class="load-more">Load More</div>

<section class="newsletter">
  <div class="nl-title">
    <svg width="31" height="22" viewBox="0 0 31 22" aria-hidden="true"><rect x="1" y="1" width="29" height="20" fill="#111"/><path d="M1 1 L15.5 12 L30 1 M1 21 L12 10 M30 21 L19 10" stroke="#fdde1a" stroke-width="1.6" fill="none"/></svg>
    <span>Subscribe to our Newsletter</span>
  </div>
  <div class="nl-field">Your Email Address...</div>
  <div class="nl-btn">SUBSCRIBE</div>
</section>

<footer class="site-footer">
  <div class="connect">CONNECT WITH US</div>
  <div class="social"><span></span><span></span><span></span><span></span></div>
  <nav class="foot-nav">HOME<b>|</b>GALLERY<b>|</b>SPECIALTY SERVICES<b>|</b>ABOUT<b>|</b>CONTACT</nav>
  <div class="foot-rule"></div>
  <svg class="pin" width="9" height="12" viewBox="0 0 9 12" aria-hidden="true"><path d="M4.5 0C2 0 0 2 0 4.5 0 7.8 4.5 12 4.5 12S9 7.8 9 4.5C9 2 7 0 4.5 0z" fill="#fff"/><circle cx="4.5" cy="4.5" r="1.7" fill="#000"/></svg>
  <p class="address">Brookmere Cafe, 1420 W. Alder Lane, Suite B, Chicago, IL 60626 (312) 555-0148</p>
  <p class="copyright">© Copyright 2017 Brookmere Cafe . &nbsp;Disclaimer &nbsp;| &nbsp;Privacy &nbsp;| &nbsp;Site Map</p>
</footer>
</body>
</html>
```